Girls Night Out Flyer for a female oriented event

I need a flyer to promote my event which should look "FUN" and "Sophisticated"
I would need the flyer to be 8 1/2" X 11" 300 dpi. I would need the layered .psd file as well as all the fonts. The flyer should contain the following info:

Velvet Evening Soiree CT
Friday, September 25th
6:00-10:00 PM
The Willow Hall Pavilion
14 Marlow Rd
Ashgrove, CT 06899
First 100 guests will have a chance to win $25,000 and receive a swag bag filled with gifts
$20 Advanced Admission at www.velveteveningsoireect.com
$25 at the door
(Key words)
Martini Bar
Wine Tasting
Food Sampling
Beauty Make-Overs
Fashion Shows
Psychic Readings
Shopping
Door Prizes
Swag Bag
Exhibitors
For tickets visit www.velveteveningsoireect.com

Target Market(s)

Ladies

Industry/Entity Type

Event

Requirements
Must have
• see description

```html
<!DOCTYPE html>
<html lang="en">
<head>
<meta charset="utf-8">
<title>Velvet Evening Soiree CT — Event Flyer</title>
<link rel="stylesheet" href="https://fonts.googleapis.com/css2?family=Poppins:wght@500;600;700&family=Questrial&display=swap">
<style>
  :root {
    --ice-blue: #a9c5d3;
    --ink: #0b0b0b;
    --paper: #ffffff;
    --backdrop: #e8eaed;
    --photo-light: #8e8e8e;
  }
  * { margin: 0; padding: 0; box-sizing: border-box; }
  html, body {
    width: 969px; height: 1200px; overflow: hidden;
    background: var(--backdrop);
  }
  .flyer {
    position: absolute; left: 54px; top: 25px;
    width: 860px; height: 1150px; overflow: hidden;
    background: var(--ice-blue);
    font-family: "Poppins", sans-serif;
  }
  .flyer__shapes { position: absolute; inset: 0; }
  .hero-photo { position: absolute; left: 575px; top: 100px; }
  .tilted {
    position: absolute; white-space: nowrap;
    transform-origin: 0 100%;
    transform: rotate(-14deg);
    line-height: 1;
  }
  .tilted--top { transform-origin: 0 0; }
  .title { color: var(--ice-blue); font-weight: 700; }
  .title--top { left: 10px; top: 292px; font-size: 104px; letter-spacing: -5px; }
  .title--middle { left: 4px; top: 429px; font-size: 124px; letter-spacing: -7px; font-weight: 600; }
  .title--bottom { left: 270px; top: 506px; font-size: 76px; letter-spacing: -4px; }
  .title__state { font-size: 28px; letter-spacing: 0; font-weight: 500; margin-left: 6px; }
  .event-date {
    left: 22px; top: 620px; color: var(--ice-blue);
    font-family: "Questrial", sans-serif; font-size: 25px; line-height: 1.05;
  }
  .event-venue {
    left: 44px; top: 678px; color: var(--ice-blue);
    font-family: "Questrial", sans-serif; font-size: 17px; letter-spacing: 1px;
  }
  .prize {
    left: 335px; top: 700px; color: var(--ink); text-align: center;
    font-family: "Questrial", sans-serif; line-height: 1.1;
  }
  .prize__intro, .prize__gift { font-size: 18px; }
  .prize__headline { font-size: 31px; font-family: "Poppins", sans-serif; font-weight: 500; }
  .admission {
    left: 40px; top: 892px; color: var(--ink); font-weight: 600;
    transform: rotate(-11deg); line-height: 1.35;
  }
  .admission__advance { font-size: 20px; }
  .admission__site { font-size: 17px; }
  .admission__door { font-size: 29px; margin-top: 8px; }
  .highlights {
    left: 404px; top: 822px; list-style: none; color: var(--ink);
    font-size: 20px; font-weight: 600; letter-spacing: 0.3px;
  }
  .highlights li { margin-bottom: 28px; }
  .tickets {
    left: 474px; top: 1084px; color: var(--ice-blue);
    font-size: 15px; font-weight: 500;
  }
</style>
</head>
<body>
<main class="flyer">
  <svg class="flyer__shapes" width="860" height="1150" viewBox="0 0 860 1150" aria-hidden="true">
    <rect class="corner-block" x="0" y="0" width="225" height="70" fill="var(--ink)"/>
    <polygon class="headline-band" points="0,125 860,-90 860,570 0,762" fill="var(--ink)"/>
    <polygon class="highlights-panel" points="371,810 860,687 860,969 431,1072" fill="var(--paper)"/>
    <polygon class="footer-band" points="431,1072 860,969 860,1150 446,1150" fill="var(--ink)"/>
    <polygon class="footer-tab" points="667,1122 847,1078 854,1106 674,1150" fill="var(--ice-blue)"/>
  </svg>

  <svg class="hero-photo" role="img" aria-label="Black and white glamour photo of a seated woman holding a clutch, wearing heels"
       width="285" height="440" viewBox="0 0 285 440">
    <defs>
      <radialGradient id="hero-tone" cx="0.5" cy="0.45" r="0.6">
        <stop offset="0" stop-color="var(--photo-light)"/>
        <stop offset="1" stop-color="var(--ink)"/>
      </radialGradient>
    </defs>
    <rect width="285" height="440" fill="url(#hero-tone)"/>
  </svg>

  <h1 class="event-title">
    <span class="tilted title title--top">VELVET</span>
    <span class="tilted title title--middle">Evening</span>
    <span class="tilted title title--bottom">SOIREE<span class="title__state">ct</span></span>
  </h1>

  <p class="tilted event-date">FRIDAY, SEPTEMBER<br>25th 6:00-10:00 PM</p>
  <p class="tilted event-venue">THE WILLOW HALL PAVILION 14 MARLOW RD, ASHGROVE, CT 06899</p>

  <p class="tilted tilted--top prize">
    <span class="prize__intro">FIRST 100 GUESTS WILL HAVE A CHANCE TO</span><br>
    <span class="prize__headline">WIN $25,000 AND RECEIVE</span><br>
    <span class="prize__gift">A SWAG BAG FILLED WITH GIFTS</span>
  </p>

  <div class="tilted tilted--top admission">
    <p class="admission__advance">$20 ADVANCED ADMISSION AT</p>
    <p class="admission__site">WWW.VELVETEVENINGSOIREECT.COM</p>
    <p class="admission__door">$25 AT THE DOOR</p>
  </div>

  <ul class="tilted tilted--top highlights">
    <li>MARTINI BAR | WINE TASTING</li>
    <li>FOOD SAMPLING | BEAUTY MAKE-OVERS</li>
    <li>FASHION SHOWS | PSYCHIC READINGS</li>
    <li>SHOPPING | DOOR PRIZES</li>
    <li>SWAG BAG | EXHIBITORS</li>
  </ul>

  <p class="tilted tilted--top tickets">For tickets visit www.velveteveningsoireect.com</p>
</main>
</body>
</html>
```